REDESIGN SIGN UP PAGE - EASY TO READ AND UNDERSTAND QUICKLY

I need to redesign my sign up page DESKTOP AND MOBILE VERSION to include 2 products that are each available as a monthly subscription, 6 mth or 12 mth subscription.

Currently I only promote one product on my website but now will be two. https://www.brightlanepromoworks.biz/signup

Now I will have two products:

1. UNLIMITED VACATION CERTIFICATES, DINING VOUCHERS & SAVINGS INCENTIVES
Unlimited Monthly Plan $99 / Month + $199 One-Time Set-Up Fee
Unlimited Bi Annual Plan $490 / 6 Months + $199 One-Time Set-Up Fee
Unlimited Annual Plan $898 / 12 Months + $199 One-Time Set-Up Fee

2. UNLIMITED SMART DEVICE INCENTIVES & OTHER HARD PREMIUMS
Unlimited Monthly Plan $299 / Month + $199 One-Time Set-Up Fee
Unlimited Bi Annual Plan $1,590 / 6 Months + $199 One-Time Set-Up Fee
Unlimited Annual Plan $2,898 / 12 Months + $199 One-Time Set-Up Fee

When promoting the different plans you can see the different categories of incentives I offer here: https://www.brightlanepromoworks.biz/incentives

The SMART DEVICE CERTIFICATES & INCENTIVES category is for product #2 and all the rest of the Categories is for Product #1 Feel free to use images as a visual so customers can see that this product includes Vacations & Restaurants and this product includes only smart devices....

USE ALL CURRENT BULLET POINTS FOR BOTH PLANS THAT IS CURRENTLY ON WEBSITE. USE ALL CURRENT CONTENT ON WEBSITE ORIGINAL SIGN UP PAGE. DO NOT LEAVE ANY CONTENT OUT.

Target Market(s)

BUSINESS OWNERS

Industry/Entity Type

Marketing

Number of Pages Required

2 page

Requirements
Must have
• When promoting the 2 different products on the new sign up page you can see the different categories of incentives I offer here: https://www.brightlanepromoworks.biz/incentives fee; free to use images to showcase what each product offers.

The SMART DEVICE CERTIFICATES & INCENTIVES category is for product #2 and all the rest of the Categories is for Product #1

I want the user to easily understand we have two products that are available in 3 ways, monthly subscription, bi annual and annual and can see the price immediately for all 3 options for both products without toggling, etc.

Must be super clean easy to ready design. Not too busy at all please
Nice to have
• USE ALL CURRENT BULLET POINTS FOR BOTH PLANS THAT IS CURRENTLY ON WEBSITE. USE ALL CURRENT CONTENT ON WEBSITE ORIGINAL SIGN UP PAGE. DO NOT LEAVE ANY CONTENT OUT.

Should not have

```html
<!DOCTYPE html>
<html lang="en">
<head>
<meta charset="utf-8">
<title>Sign Up – Brightlane Promo Works</title>
<link href="https://fonts.googleapis.com/css2?family=Montserrat:wght@800;900&family=Poppins:wght@400;500;600;700&display=swap" rel="stylesheet">
<style>
:root{
  --blue:#1a73c6;
  --blue-dark:#0f5ea8;
  --green:#17a84a;
  --green-dark:#108a3a;
  --navy:#102a40;
  --navy-deep:#0b1f31;
  --ink:#111;
  --text:#555;
  --muted:#8a96a3;
  --white:#fff;
  --card-shadow:0 2px 10px rgba(0,0,0,.12);
}
*{box-sizing:border-box;margin:0;padding:0}
html,body{width:1200px;height:3993px;overflow:hidden;background:var(--white);font-family:'Poppins',sans-serif;color:var(--text)}
.page{position:relative;width:1200px;height:3993px}

/* header */
.site-header{position:absolute;top:0;left:0;width:1200px;height:77px;display:flex}
.brand{width:270px;display:flex;align-items:center;gap:10px;padding-left:18px;background:var(--white)}
.brand-mark{width:26px;height:26px;border-radius:50%;background:var(--blue);flex:none}
.brand-name{font-weight:600;font-size:15px;color:var(--blue);line-height:1.1}
.main-nav{flex:1;background:var(--blue);display:flex;align-items:center;gap:22px;padding-left:48px;clip-path:polygon(28px 0,100% 0,100% 100%,0 100%)}
.main-nav a{color:var(--white);font-size:12px;font-weight:500;text-decoration:none;white-space:nowrap}
.nav-tool{width:63px;background:var(--blue-dark);display:flex;flex-direction:column;align-items:center;justify-content:center;gap:6px;color:var(--white);font-size:10px;font-weight:500;white-space:nowrap}
.nav-tool+.nav-tool{background:var(--blue)}
.call-box{width:210px;background:var(--green);display:flex;align-items:center;gap:12px;padding-left:14px;color:var(--white);font-size:11.5px;font-weight:700;line-height:1.6;white-space:nowrap}

/* intro */
.intro{position:absolute;top:128px;left:0;width:1200px;text-align:center}
.intro h1{font-family:'Montserrat',sans-serif;font-weight:900;font-size:42px;line-height:62px;color:var(--ink);text-transform:uppercase;letter-spacing:-.5px}
.intro p{margin-top:40px;font-size:28px;line-height:47px;color:#444}

/* banners */
.product-banner{position:absolute;left:111px;width:978px;height:291px;display:flex;align-items:center;justify-content:center;text-align:center}
.product-banner h2{position:relative;font-family:'Montserrat',sans-serif;font-weight:900;font-size:39px;line-height:55px;color:var(--white);text-shadow:0 2px 6px rgba(0,0,0,.45)}
.banner-art{position:absolute;inset:0}
.banner-notch{position:absolute;bottom:0;left:50%;width:0;height:0;transform:translateX(-50%);border-left:18px solid transparent;border-right:18px solid transparent;border-bottom:16px solid var(--white)}
.banner-dining{top:487px}
.banner-dining .banner-art{background:linear-gradient(120deg,#4a3a2e,#8c6f55 45%,#5d4a3c)}
.banner-devices{top:1985px}
.banner-devices .banner-art{background:linear-gradient(120deg,#2d3238,#5a636c 50%,#3a4047)}

/* plans */
.plan-row{position:absolute;left:111px;width:978px;display:flex;gap:21px}
.plan-row.first{top:813px}
.plan-row.second{top:2311px}
.plan-card{width:312px;height:1119px;background:var(--white);box-shadow:var(--card-shadow);position:relative}
.plan-head{height:147px;background:var(--blue);color:var(--white);text-align:center;padding-top:14px;white-space:nowrap}
.plan-card.featured .plan-head{background:var(--green)}
.plan-title{font-size:24px;font-weight:600;line-height:30px}
.plan-sub{font-size:12.5px;margin-top:3px}
.plan-price{margin-top:10px;font-size:16px;font-weight:600}
.plan-price strong{font-size:31px;font-weight:700}
.plan-fee{font-size:15px;font-weight:600;margin-top:2px}
.feature-list{list-style:none;padding:29px 8px 0 42px}
.feature-list li{position:relative;font-size:13.4px;line-height:17px;margin-bottom:17px;color:var(--text);white-space:nowrap}
.feature-list li::before{content:"";position:absolute;left:-21px;top:1px;width:6px;height:11px;border:solid var(--blue);border-width:0 3px 3px 0;transform:rotate(45deg)}
.plan-card.featured .feature-list li::before{border-color:var(--green)}
.select-btn{position:absolute;left:50%;bottom:22px;transform:translateX(-50%);width:155px;height:58px;background:var(--blue);color:var(--white);font-size:21px;font-weight:600;display:flex;align-items:center;justify-content:center;text-decoration:none}
.plan-card.featured .select-btn{background:var(--green)}

/* footer */
.site-footer{position:absolute;top:3505px;left:0;width:1200px;height:488px;background:linear-gradient(180deg,var(--navy),var(--navy-deep));color:#c7d2dc}
.footer-accent{position:absolute;top:0;left:270px;width:930px;height:3px;background:var(--blue)}
.footer-brand{position:absolute;left:35px;top:40px;width:265px;text-align:center}
.footer-brand .brand-mark{display:block;margin:0 auto 10px;width:34px;height:34px}
.footer-brand .brand-name{font-size:20px;color:var(--blue);white-space:nowrap}
.socials{display:flex;justify-content:center;gap:14px;margin-top:28px}
.socials span{width:39px;height:39px;border-radius:50%;background:#55606b}
.samples-btn{display:block;margin:32px auto 0;width:255px;height:60px;background:var(--green);color:var(--white);font-weight:700;font-size:14px;line-height:18px;padding-top:12px;text-decoration:none;clip-path:polygon(0 0,100% 0,96% 100%,4% 100%)}
.samples-btn small{display:block;font-size:11px;font-weight:600}
.footer-col{position:absolute;top:46px}
.footer-col h3{font-family:'Montserrat',sans-serif;font-weight:900;font-size:18px;color:var(--white);margin-bottom:22px}
.footer-col a,.footer-col p{display:block;font-size:12.5px;line-height:18px;color:#c7d2dc;text-decoration:none}
.col-contact{left:348px;width:300px}
.col-quick{left:710px;width:180px}
.col-other{left:927px;width:250px}
.col-quick a,.col-other a{margin-bottom:9.5px}
.contact-item{position:relative;padding-left:24px;margin-bottom:14px}
.contact-item svg{position:absolute;left:0;top:2px}
.contact-item b{color:var(--white);font-weight:600}
.contact-item .hl{color:#2aa853}
.footer-bottom{position:absolute;left:35px;right:35px;bottom:20px;display:flex;justify-content:space-between;font-size:12.5px;color:#9aa8b5}
.footer-bottom b{color:var(--white);font-weight:600}
.footer-bottom .hl{color:var(--blue)}
.chat-bubble{position:absolute;right:60px;bottom:18px;width:52px;height:52px;border-radius:50%;background:#e0242a}
</style>
</head>
<body>
<div class="page">

<header class="site-header">
  <div class="brand"><span class="brand-mark"></span><span class="brand-name">Brightlane<br>Promo Works</span></div>
  <nav class="main-nav">
    <a href="#">Home</a><a href="#">The Incentives</a><a href="#">Samples</a><a href="#">Industries</a><a href="#">Testimonials</a><a href="#">Faq</a><a href="#">Integrations</a>
  </nav>
  <div class="nav-tool">
    <svg width="18" height="18" viewBox="0 0 18 18"><circle cx="9" cy="5" r="4" fill="#fff"/><path d="M1 18c0-5 4-7 8-7s8 2 8 7z" fill="#fff"/></svg>LOGIN</div>
  <div class="nav-tool">
    <svg width="18" height="18" viewBox="0 0 18 18"><circle cx="9" cy="9" r="8" fill="none" stroke="#fff" stroke-width="2"/><path d="M9 13V5M5.5 8.5L9 5l3.5 3.5" fill="none" stroke="#fff" stroke-width="2"/></svg>SIGN UP</div>
  <div class="call-box">
    <svg width="20" height="34" viewBox="0 0 20 34"><rect x="1" y="1" width="18" height="32" rx="3" fill="none" stroke="#fff" stroke-width="2"/><circle cx="10" cy="28" r="1.8" fill="#fff"/></svg>
    <div>CALL US: 1-555-204-7781<br>TEXT US: 1-555-318-4402</div>
  </div>
</header>

<section class="intro">
  <h1>Congratulations on making the<br>decision to make more money for<br>your business</h1>
  <p>This program is an online subscription based incentive<br>marketing system with the following features</p>
</section>

<section class="product-banner banner-dining">
  <div class="banner-art" role="img" aria-label="Restaurant table with plated dishes and drinks"></div>
  <h2>Unlimited Vacation Certificates,<br>Dining Vouchers &amp; Savings Incentives</h2>
  <span class="banner-notch"></span>
</section>

<div class="plan-row first">
  <article class="plan-card">
    <div class="plan-head"><div class="plan-title">Unlimited Monthly Plan</div><div class="plan-sub">One Account Can Be Used For Unlimited</div><div class="plan-price"><strong>$99</strong> / Month +</div><div class="plan-fee">$199 One-Time Set-Up Fee</div></div>
    <ul class="feature-list">
      <li>Unlimited E-Certificates</li><li>Unlimited SMS Certificates</li><li>Unlimited Web Banner Certificates</li><li>Unlimited White Label Certificate<br>Landing Pages</li><li>Unlimited Website Sticky<br>Bar Certificates</li><li>Unlimited Website Pop Up<br>Certificate</li><li>Unlimited API E-Certificates</li><li>Unlimited Linkwise Integration Access</li><li>FREE Warm Lead Letter Templates</li><li>FREE Customer Appreciation<br>Letter Templates</li><li>FREE Professional-Grade<br>Incentive Videos</li><li>FREE Proven Chatterly™<br>Ad Templates</li><li>FREE High-Converting Banner<br>Ad Templates</li><li>FREE Time-Tested Print<br>Ad Templates</li><li>FREE White Label Redemption<br>Website</li><li>FREE Industry Specific Ad Packs</li><li>FREE Affiliate Program-Earn<br>50% Commissions</li><li>FREE Eye-Catching Posters,<br>Flyers &amp; Brochures Each Certificate</li><li>FREE Step by Step Redemption<br>Guides</li>
    </ul>
    <a class="select-btn" href="#">SELECT</a>
  </article>
  <article class="plan-card featured">
    <div class="plan-head"><div class="plan-title">Unlimited Bi Annual Plan</div><div class="plan-sub">One Account Can Be Used For Unlimited</div><div class="plan-price"><strong>$490</strong> / 6 Months +</div><div class="plan-fee">$199 One-Time Set-Up Fee</div></div>
    <ul class="feature-list">
      <li>Unlimited E-Certificates</li><li>Unlimited SMS Certificates</li><li>Unlimited Web Banner Certificates</li><li>Unlimited White Label Certificate<br>Landing Pages</li><li>Unlimited Website Sticky<br>Bar Certificates</li><li>Unlimited Website Pop Up<br>Certificate</li><li>Unlimited API E-Certificates</li><li>Unlimited Linkwise Integration Access</li><li>FREE Warm Lead Letter Templates</li><li>FREE Customer Appreciation<br>Letter Templates</li><li>FREE Professional-Grade<br>Incentive Videos</li><li>FREE Proven Chatterly™<br>Ad Templates</li><li>FREE High-Converting Banner<br>Ad Templates</li><li>FREE Time-Tested Print<br>Ad Templates</li><li>FREE White Label Redemption<br>Website</li><li>FREE Industry Specific Ad Packs</li><li>FREE Affiliate Program-Earn<br>50% Commissions</li><li>FREE Eye-Catching Posters,<br>Flyers &amp; Brochures Each Certificate</li><li>FREE Step by Step Redemption<br>Guides</li>
    </ul>
    <a class="select-btn" href="#">SELECT</a>
  </article>
  <article class="plan-card">
    <div class="plan-head"><div class="plan-title">Unlimited Annual Plan</div><div class="plan-sub">One Account Can Be Used For Unlimited</div><div class="plan-price"><strong>$898</strong> / 12 Months +</div><div class="plan-fee">$199 One-Time Set-Up Fee</div></div>
    <ul class="feature-list">
      <li>Unlimited E-Certificates</li><li>Unlimited SMS Certificates</li><li>Unlimited Web Banner Certificates</li><li>Unlimited White Label Certificate<br>Landing Pages</li><li>Unlimited Website Sticky<br>Bar Certificates</li><li>Unlimited Website Pop Up<br>Certificate</li><li>Unlimited API E-Certificates</li><li>Unlimited Linkwise Integration Access</li><li>FREE Warm Lead Letter Templates</li><li>FREE Customer Appreciation<br>Letter Templates</li><li>FREE Professional-Grade<br>Incentive Videos</li><li>FREE Proven Chatterly™<br>Ad Templates</li><li>FREE High-Converting Banner<br>Ad Templates</li><li>FREE Time-Tested Print<br>Ad Templates</li><li>FREE White Label Redemption<br>Website</li><li>FREE Industry Specific Ad Packs</li><li>FREE Affiliate Program-Earn<br>50% Commissions</li><li>FREE Eye-Catching Posters,<br>Flyers &amp; Brochures Each Certificate</li><li>FREE Step by Step Redemption<br>Guides</li>
    </ul>
    <a class="select-btn" href="#">SELECT</a>
  </article>
</div>

<section class="product-banner banner-devices">
  <div class="banner-art" role="img" aria-label="Laptop and smart devices on a desk"></div>
  <h2>Unlimited Smart Device Incentives<br>&amp; Other Hard Premiums</h2>
  <span class="banner-notch"></span>
</section>

<div class="plan-row second">
  <article class="plan-card">
    <div class="plan-head"><div class="plan-title">Unlimited Monthly Plan</div><div class="plan-sub">One Account Can Be Used For Unlimited</div><div class="plan-price"><strong>$299</strong> / Month +</div><div class="plan-fee">$199 One-Time Set-Up Fee</div></div>
    <ul class="feature-list">
      <li>Unlimited E-Certificates</li><li>Unlimited SMS Certificates</li><li>Unlimited Web Banner Certificates</li><li>Unlimited White Label Certificate<br>Landing Pages</li><li>Unlimited Website Sticky<br>Bar Certificates</li><li>Unlimited Website Pop Up<br>Certificate</li><li>Unlimited API E-Certificates</li><li>Unlimited Linkwise Integration Access</li><li>FREE Warm Lead Letter Templates</li><li>FREE Customer Appreciation<br>Letter Templates</li><li>FREE Professional-Grade<br>Incentive Videos</li><li>FREE Proven Chatterly™<br>Ad Templates</li><li>FREE High-Converting Banner<br>Ad Templates</li><li>FREE Time-Tested Print<br>Ad Templates</li><li>FREE White Label Redemption<br>Website</li><li>FREE Industry Specific Ad Packs</li><li>FREE Affiliate Program-Earn<br>50% Commissions</li><li>FREE Eye-Catching Posters,<br>Flyers &amp; Brochures Each Certificate</li><li>FREE Step by Step Redemption<br>Guides</li>
    </ul>
    <a class="select-btn" href="#">SELECT</a>
  </article>
  <article class="plan-card">
    <div class="plan-head"><div class="plan-title">Unlimited Bi Annual Plan</div><div class="plan-sub">One Account Can Be Used For Unlimited</div><div class="plan-price"><strong>$1,590</strong> / 6 Months +</div><div class="plan-fee">$199 One-Time Set-Up Fee</div></div>
    <ul class="feature-list">
      <li>Unlimited E-Certificates</li><li>Unlimited SMS Certificates</li><li>Unlimited Web Banner Certificates</li><li>Unlimited White Label Certificate<br>Landing Pages</li><li>Unlimited Website Sticky<br>Bar Certificates</li><li>Unlimited Website Pop Up<br>Certificate</li><li>Unlimited API E-Certificates</li><li>Unlimited Linkwise Integration Access</li><li>FREE Warm Lead Letter Templates</li><li>FREE Customer Appreciation<br>Letter Templates</li><li>FREE Professional-Grade<br>Incentive Videos</li><li>FREE Proven Chatterly™<br>Ad Templates</li><li>FREE High-Converting Banner<br>Ad Templates</li><li>FREE Time-Tested Print<br>Ad Templates</li><li>FREE White Label Redemption<br>Website</li><li>FREE Industry Specific Ad Packs</li><li>FREE Affiliate Program-Earn<br>50% Commissions</li><li>FREE Eye-Catching Posters,<br>Flyers &amp; Brochures Each Certificate</li><li>FREE Step by Step Redemption<br>Guides</li>
    </ul>
    <a class="select-btn" href="#">SELECT</a>
  </article>
  <article class="plan-card">
    <div class="plan-head"><div class="plan-title">Unlimited Annual Plan</div><div class="plan-sub">One Account Can Be Used For Unlimited</div><div class="plan-price"><strong>$2,898</strong> / 12 Months +</div><div class="plan-fee">$199 One-Time Set-Up Fee</div></div>
    <ul class="feature-list">
      <li>Unlimited E-Certificates</li><li>Unlimited SMS Certificates</li><li>Unlimited Web Banner Certificates</li><li>Unlimited White Label Certificate<br>Landing Pages</li><li>Unlimited Website Sticky<br>Bar Certificates</li><li>Unlimited Website Pop Up<br>Certificate</li><li>Unlimited API E-Certificates</li><li>Unlimited Linkwise Integration Access</li><li>FREE Warm Lead Letter Templates</li><li>FREE Customer Appreciation<br>Letter Templates</li><li>FREE Professional-Grade<br>Incentive Videos</li><li>FREE Proven Chatterly™<br>Ad Templates</li><li>FREE High-Converting Banner<br>Ad Templates</li><li>FREE Time-Tested Print<br>Ad Templates</li><li>FREE White Label Redemption<br>Website</li><li>FREE Industry Specific Ad Packs</li><li>FREE Affiliate Program-Earn<br>50% Commissions</li><li>FREE Eye-Catching Posters,<br>Flyers &amp; Brochures Each Certificate</li><li>FREE Step by Step Redemption<br>Guides</li>
    </ul>
    <a class="select-btn" href="#">SELECT</a>
  </article>
</div>

<footer class="site-footer">
  <span class="footer-accent"></span>
  <div class="footer-brand">
    <span class="brand-mark"></span>
    <div class="brand-name">Brightlane Promo Works</div>
    <div class="socials"><span></span><span></span><span></span><span></span></div>
    <a class="samples-btn" href="#">GET FREE SAMPLES<small>100% FREE</small></a>
  </div>

  <div class="footer-col col-contact">
    <h3>CONTACT US</h3>
    <div class="contact-item"><svg width="14" height="16" viewBox="0 0 14 16"><path d="M7 15s5-5 5-9A5 5 0 0 0 2 6c0 4 5 9 5 9z" fill="none" stroke="#c7d2dc" stroke-width="1.4"/><circle cx="7" cy="6" r="1.8" fill="#c7d2dc"/></svg><p><b>Brightlane Promo Works Group, Inc.</b><br>4470 Harbor Crest Way Suite 210<br>Lakemont, CA 90210</p></div>
    <div class="contact-item"><svg width="14" height="14" viewBox="0 0 14 14"><path d="M3 1l2.5 3-1.5 1.5c1 2 2.5 3.5 4.5 4.5L10 8.5l3 2.5-1.5 2C6 13 1 8 1 2.5z" fill="none" stroke="#c7d2dc" stroke-width="1.3"/></svg><p>USA Office: <b>1-555-204-7781</b><br>International: <b>1-800-555-0142</b><br>Text Us: <b>1-555-330-9164</b></p></div>
    <div class="contact-item"><svg width="14" height="12" viewBox="0 0 14 12"><rect x="1" y="1" width="12" height="10" fill="none" stroke="#c7d2dc" stroke-width="1.3"/><path d="M1 1l6 5 6-5" fill="none" stroke="#c7d2dc" stroke-width="1.3"/></svg><p>hello@brightlanepromoworks.biz</p></div>
    <div class="contact-item"><svg width="14" height="14" viewBox="0 0 14 14"><circle cx="7" cy="7" r="6" fill="none" stroke="#c7d2dc" stroke-width="1.3"/><path d="M7 3.5V7l2.5 1.5" fill="none" stroke="#c7d2dc" stroke-width="1.3"/></svg><p>24/7 Chat Support<br>24/7 Live Answering Service<br>24/7 Email Support<br><span class="hl">Live Phone &amp; SMS Support:</span><br>Monday - Friday 8am - 5pm PST<br><span class="hl">Sat/Sun/Holidays Closed</span></p></div>
  </div>

  <div class="footer-col col-quick">
    <h3>QUICK LINKS</h3>
    <a href="#">Home</a><a href="#">The Incentives</a><a href="#">Samples</a><a href="#">Affiliate</a><a href="#">Testimonials</a><a href="#">Faq</a><a href="#">Contact Us</a><a href="#">Redemption Demo<br>Videos</a><a href="#">BPW Distribute Certificate<br>Demo Videos</a>
  </div>

  <div class="footer-col col-other">
    <h3>OTHER LINKS</h3>
    <a href="#">Hoteliers</a><a href="#">Bpw Certificates List</a><a href="#">How To Use Bpw Certificates</a><a href="#">Chatterly Incentive Campaign</a><a href="#">Pop Ups &amp; Sticky Bars</a><a href="#">Whitepaper - Increase Sales</a><a href="#">Whitepaper - Improve Sales During<br>Strange Times</a><a href="#">Whitepaper - Boost Website<br>Conversions</a>
  </div>

  <div class="footer-bottom">
    <span>© 2020 <b>Brightlane Promo Works Group, Inc.</b> All Rights Reserved. CST# 4418306 <span class="hl">TCRC#</span> 772904</span>
    <span style="margin-right:70px">Privacy Policy &nbsp;|&nbsp; Term And Conditions</span>
  </div>
  <span class="chat-bubble"></span>
</footer>

</div>
</body>
</html>
```